landscape and garden design business card

I would like a business card designed for my landscape and garden design company, Thistlecove Gardens. We are located in Colorado. I would like to include our logo, contact info, and social media/web site address or QR code. Looking for an organic, flowing design that incorporates our logo.

Target Market(s)

Homeowners and businesses that need garden and landscape design

Contact Information for Business Card

Would like it to say landscape and garden design

Requirements
Must have
• Landscape and garden design

```html
<!DOCTYPE html>
<html lang="en">
<head>
<meta charset="utf-8">
<title>Thistlecove Gardens — Business Card</title>
<link href="https://fonts.googleapis.com/css2?family=Cormorant+Garamond:wght@600&family=Poppins:wght@400;500&family=Pinyon+Script&display=swap" rel="stylesheet">
<style>
  :root {
    --stage: #8a8a8a;
    --paper: #ffffff;
    --forest: #0f2a24;
    --forest-deep: #0b221d;
    --row: #133129;
    --ink: #0e2a23;
    --light: #f4f6f4;
  }
  * { margin: 0; padding: 0; box-sizing: border-box; }
  html, body { width: 965px; height: 1200px; overflow: hidden; }
  body { background: var(--stage); position: relative; font-family: "Poppins", sans-serif; }

  .card {
    position: absolute;
    left: 176px;
    width: 612px;
    height: 349px;
    background: var(--paper);
    box-shadow: 4px 6px 9px rgba(0,0,0,.35);
    overflow: hidden;
  }
  .card--front { top: 188px; }
  .card--back { top: 651px; }

  /* brand mark */
  .brand { position: absolute; display: flex; flex-direction: column; align-items: center; }
  .brand__disc { border-radius: 50%; background: var(--forest); }
  .brand__name {
    font-family: "Cormorant Garamond", serif;
    font-weight: 600;
    color: var(--ink);
    white-space: nowrap;
    line-height: 1;
  }
  .brand__tagline {
    font-family: "Poppins", sans-serif;
    font-weight: 500;
    color: var(--ink);
    text-transform: uppercase;
    white-space: nowrap;
    line-height: 1;
  }
  .card--front .brand { left: 0; right: 0; top: 46px; }
  .card--front .brand__disc { width: 88px; height: 88px; }
  .card--front .brand__name { font-size: 30px; margin-top: 8px; }
  .card--front .brand__tagline { font-size: 10px; letter-spacing: 2.4px; margin-top: 7px; }

  /* front meadow */
  .meadow {
    position: absolute; left: 0; right: 0; top: 214px; height: 80px;
    background: linear-gradient(180deg, rgba(15,42,36,0) 0%, rgba(15,42,36,.35) 45%, var(--forest) 100%);
  }
  .ground {
    position: absolute; left: 0; right: 0; top: 292px; bottom: 0;
    background: var(--forest);
  }
  .ground__url {
    position: absolute; left: 0; right: 0; top: 14px;
    text-align: center; color: var(--light);
    font-size: 14.5px; font-weight: 500; letter-spacing: 2.2px;
  }

  /* back */
  .identity { position: absolute; left: 0; top: 0; width: 266px; height: 100%; }
  .card--back .brand { left: 0; right: 0; top: 56px; }
  .card--back .brand__disc { width: 66px; height: 66px; }
  .card--back .brand__name { font-size: 22px; margin-top: 8px; }
  .card--back .brand__tagline { font-size: 7.5px; letter-spacing: 1.6px; margin-top: 6px; }
  .person { position: absolute; left: 0; right: 0; top: 208px; text-align: center; color: var(--ink); }
  .person__name {
    display: inline-block;
    font-family: "Pinyon Script", cursive;
    font-size: 32px; line-height: 1.1;
    padding: 0 2px 1px;
    border-bottom: 1px solid var(--ink);
  }
  .person__role {
    font-family: "Cormorant Garamond", serif;
    font-weight: 600; font-size: 21px; letter-spacing: .5px;
    margin-top: 6px;
  }

  .contact {
    position: absolute; left: 266px; top: 0; right: 0; bottom: 0;
    background: linear-gradient(160deg, var(--forest) 0%, var(--forest-deep) 100%);
  }
  .contact__list { list-style: none; position: absolute; left: 0; right: 0; top: 69px; }
  .contact__item { position: relative; height: 40px; margin-bottom: 10.5px; }
  .contact__icon { position: absolute; left: 13px; top: 12px; width: 16px; height: 16px; }
  .contact__text {
    position: absolute; left: 43px; right: 12px; top: 0; height: 40px;
    background: var(--row);
    color: var(--light);
    font-size: 15.5px; line-height: 40px;
    padding-left: 10px;
    white-space: nowrap;
  }
  .contact__dot { position: absolute; left: 16px; top: 14px; width: 12px; height: 12px; border-radius: 50%; background: var(--light); }
  .contact__meadow {
    position: absolute; left: 0; right: 0; bottom: 0; height: 60px;
    background: linear-gradient(180deg, rgba(244,246,244,0) 0%, rgba(244,246,244,.45) 65%, var(--light) 100%);
  }
</style>
</head>
<body>

<section class="card card--front">
  <div class="brand">
    <div class="brand__disc"></div>
    <div class="brand__name">Thistlecove Gardens</div>
    <div class="brand__tagline">Landscape and garden design</div>
  </div>
  <div class="meadow" role="img" aria-label="Silhouette of wildflowers and meadow grasses along the bottom edge"></div>
  <div class="ground">
    <p class="ground__url">www.thistlecovegardens.com</p>
  </div>
</section>

<section class="card card--back">
  <div class="identity">
    <div class="brand">
      <div class="brand__disc"></div>
      <div class="brand__name">Thistlecove Gardens</div>
      <div class="brand__tagline">Landscape and garden design</div>
    </div>
    <div class="person">
      <div class="person__name">Maren Ashby</div>
      <div class="person__role">OWNER</div>
    </div>
  </div>

  <div class="contact">
    <ul class="contact__list">
      <li class="contact__item">
        <svg class="contact__icon" viewBox="0 0 16 16" fill="#f4f6f4"><path d="M3.5 1.5l2.4 2.6-1.3 1.8c.8 1.9 2.5 3.7 4.5 4.6l1.8-1.3 2.6 2.4-1.4 2.4C6.6 13.6 2.4 9.4 1.1 3z"/></svg>
        <span class="contact__text">(970) 555 - 0142</span>
      </li>
      <li class="contact__item">
        <svg class="contact__icon" viewBox="0 0 16 16"><rect x="1.5" y="3.5" width="13" height="9" fill="#f4f6f4"/><path d="M1.5 3.5L8 9l6.5-5.5" fill="none" stroke="#0f2a24" stroke-width="1.3"/></svg>
        <span class="contact__text">hello@thistlecovegardens.com</span>
      </li>
      <li class="contact__item">
        <svg class="contact__icon" viewBox="0 0 16 16" fill="none" stroke="#f4f6f4" stroke-width="1.4"><circle cx="8" cy="8" r="6.5"/><ellipse cx="8" cy="8" rx="2.8" ry="6.5"/><path d="M1.5 8h13"/></svg>
        <span class="contact__text">www.thistlecovegardens.com</span>
      </li>
      <li class="contact__item">
        <span class="contact__dot"></span>
        <span class="contact__text">@thistlecovegardens #gardens</span>
      </li>
    </ul>
    <div class="contact__meadow" role="img" aria-label="Light silhouette of wildflowers and grasses along the bottom edge"></div>
  </div>
</section>

</body>
</html>
```